New Design for Accounting Firm

CLIENT NAME: Corvantel
CURRENT WEBSITE: www.corvantelgroup.com.au

CLIENTS THE CLIENT LIKES:
http://vetrulka.se/
http://www.markoplex.biz/index.php
http://www.frendaworks.co.uk/
http://www.brightharbourrelief.org/

COLOUR THEMES:
Colour theme to reflect the logo, with a leaning to blue in Accounting & Audit sections and green in Super section.

LOOK AND FEEL:
The look and feel needs to reflect an accessible culture and contemporary sensibility while still communicating our experience and stability as a professional company.

ABOUT:
The concept of 'Corvantel' is integral to our identity. Definition: 'The connection of creative ideas from a group of diverse individuals, applied with the end aim of solving practical problems'. See ''About Us'' on our website for more.

OTHER DETAILS:
Our three divisions (and service areas within each division) must be easily navigated as they related to very different users of the site. Two client sign in sections (Accounting & Super) must be easily distinguished to avoid user confusion.

MENU STRUCTURE:
* About
- includes history, values, our people, community etc
* Accounting & Advisory
- About
- Services
- Tax & Accounting
- Business Advisory
- Family Wealth Management
- Client Sign In
- Calculators
* Audit & Assurance
- About
- Services
* Corvantel Super
- About
- Individuals
- Services
- Advisers
- Services
- Portal Sign In
- Calculators
* Careers
* Newsletters
* Contact

REQUIREMENTS:
- Layered PSD form home and content pages
- No coding required, we use our own CMS to insert XHTML files into.
Updates

Hi Guys,

The client has asked for a non-cliche'd images in the design. If you'd like to try again with some images that represent the business but aren't your standard boring accounting-looking people, then please do! Cliche is a killer in design - please pump some creativity in!

Cheers,
Ned.

Reason: GUYS - PLEASE LISTEN TO THESE COMMENTS - I'VE SAID THEM TWICE NOW AND PEOPLE ARE STILL POSTING PROJECTS WITH CLICHED AND OBVIOUS ACCOUTNING TYPE IMAGES. USE YOUR CREATIVITY AND POST A DESIGN THAT IS OUTSIDE THE BOX WITH REGARDS TO THE IMAGES YOU ARE USING.

Reason: I am waiting to hear back from the client on their decision.

```html
<!DOCTYPE html>
<html lang="en">
<head>
<meta charset="utf-8">
<title>Corvantel – Accounting, Audit and Super</title>
<link rel="stylesheet" href="https://fonts.googleapis.com/css2?family=Arimo:wght@400;700&display=swap">
<style>
:root{
  --blue:#1568a8;
  --blue-dark:#0c3a78;
  --blue-deep:#082c60;
  --green:#5dbb63;
  --green-dark:#3f9a45;
  --green-light:#8fd06b;
  --lime:#9bd16a;
  --grey-bg:#f4f4f4;
  --panel:#ffffff;
  --text:#1f1f1f;
  --footer:#383838;
  --footer-line:#5a5a5a;
  --white:#ffffff;
}
*{margin:0;padding:0;box-sizing:border-box}
html,body{width:1200px;height:1158px;overflow:hidden}
body{font-family:"Arimo",Arial,sans-serif;color:var(--text);background:var(--grey-bg);position:relative}
.site-header{height:103px;background:var(--white);position:relative}
.brand{position:absolute;left:104px;top:26px;display:flex;align-items:center;gap:12px}
.brand-square{width:44px;height:44px;background:var(--blue)}
.brand-name{font-size:52px;font-weight:400;color:var(--blue);letter-spacing:-1px;line-height:1}

.main-nav{height:47px;background:linear-gradient(#6cc66f,#54b25a);position:relative;border-bottom:2px solid #4aa550}
.main-nav ul{list-style:none;display:flex;position:absolute;left:105px;top:14px}
.main-nav li{color:var(--white);font-weight:700;font-size:16.5px;display:flex;align-items:center;white-space:nowrap}
.main-nav li+li::before{content:"|";margin:0 13px;font-weight:400}
.main-nav .current{position:relative}
.main-nav .current::after{content:"";position:absolute;left:50%;bottom:-19px;margin-left:-7px;border:7px solid transparent;border-bottom-color:var(--blue-dark)}

.hero{height:252px;position:relative;background:linear-gradient(100deg,var(--blue-deep) 0%,var(--blue-dark) 45%,#1b6fb0 100%);overflow:hidden}
.hero-art{position:absolute;right:0;top:0;width:640px;height:252px;background:linear-gradient(90deg,rgba(30,120,190,0) 0%,rgba(40,140,210,.55) 60%,rgba(30,120,190,.4) 100%)}
.hero-title{position:absolute;left:104px;top:50px;color:var(--white);font-size:28.5px;font-weight:700;line-height:35px}
.hero-title em{font-style:normal;color:var(--green-light)}
.hero-actions{position:absolute;left:103px;top:179px;display:flex;gap:12px}
.btn{display:flex;align-items:center;justify-content:space-between;height:39px;padding:0 10px 0 15px;border-radius:4px;color:var(--white);font-weight:700;font-size:16px;white-space:nowrap;border:1px solid rgba(255,255,255,.35)}
.btn-green{background:linear-gradient(#6fcf5a,#3f9f3c);width:182px}
.btn-grey{background:linear-gradient(#9a9a9a,#5e5e5e);width:145px}
.btn-icon{width:20px;height:20px;flex:none;margin-left:8px}

.intro{position:absolute;left:104px;top:430px;width:648px}
.intro h1{font-size:24px;color:var(--blue);font-weight:700;margin-bottom:14px}
.intro p{font-size:15.6px;line-height:18.4px;text-align:justify;margin-bottom:19px}

.signin{position:absolute;left:792px;top:432px;width:319px}
.signin-title{display:flex;align-items:center;gap:9px;color:var(--blue);font-weight:700;font-size:17px;margin-left:4px}
.signin-tabs{display:flex;margin-top:14px;height:35px}
.signin-tab{width:121px;border-radius:6px 6px 0 0;display:flex;align-items:center;justify-content:center;font-weight:700;font-size:16px;color:var(--blue)}
.signin-tab.active{background:var(--panel)}
.signin-tab.inactive{background:#e0e0e0;margin-left:7px;width:119px}
.signin-form{background:var(--panel);border-radius:0 6px 6px 6px;height:176px;padding:16px 19px}
.signin-form label{display:block;font-size:15.6px;margin-bottom:5px}
.field{width:210px;height:27px;border:1px solid #999;background:var(--white);margin-bottom:18px;box-shadow:inset 0 1px 2px rgba(0,0,0,.15)}
.signin-actions{display:flex;align-items:center;gap:8px;margin-top:-6px}
.btn-login{display:flex;align-items:center;height:26px;width:88px;border-radius:3px;background:linear-gradient(#9d9d9d,#666);color:var(--white);font-weight:700;font-size:14.5px}
.btn-login span{flex:1;text-align:center}
.btn-login b{width:24px;border-left:1px solid #888;text-align:center;font-size:15px}
.forgot{color:var(--blue);font-size:14.5px;text-decoration:underline;white-space:nowrap}

.divisions{position:absolute;left:101px;top:710px;width:1011px;height:171px;display:flex;background:linear-gradient(#ffffff,#f1f1f1);border:1px solid #d8d8d8;border-radius:5px}
.division{flex:1;position:relative;padding:14px 22px 0 22px;border-right:1px solid #d8d8d8}
.division:last-child{border-right:0}
.division h2{color:var(--blue);font-size:17px;font-weight:700;margin-bottom:6px;white-space:nowrap}
.division p{font-size:13.4px;line-height:16.8px;text-align:justify;height:68px;overflow:hidden}
.btn-more{display:inline-flex;align-items:center;height:26px;margin-top:8px;border-radius:3px;background:linear-gradient(#8dcc5b,#4c9e33);color:var(--white);font-size:14px;font-weight:700;border:1px solid #3f8a2b;white-space:nowrap}
.btn-more span{padding:0 8px}
.btn-more b{border-left:1px solid #6bb54a;padding:0 6px}
.division::after{content:"";position:absolute;right:0;bottom:0;border-style:solid;border-width:0 0 22px 22px;border-color:transparent transparent var(--blue) transparent}

.site-footer{position:absolute;left:0;top:924px;width:1200px;height:234px;background:var(--footer);box-shadow:0 -6px 14px rgba(0,0,0,.15)}
.footer-col{position:absolute;top:23px;width:190px}
.footer-col h3{color:var(--lime);font-size:16px;font-weight:700;margin-bottom:6px;white-space:nowrap}
.footer-col ul{list-style:none}
.footer-col li{color:var(--white);font-size:13px;height:24px;line-height:22px;border-bottom:1px solid var(--footer-line);white-space:nowrap}
.footer-col li:last-child{border-bottom:0}
.footer-col .link-heading{color:var(--lime);font-size:16px;font-weight:700;height:26px;line-height:26px;border-bottom:1px solid var(--footer-line)}
.footer-contact{position:absolute;left:811px;top:21px;width:290px;color:var(--white);font-size:14px;line-height:17.5px}
.footer-contact h3{color:var(--lime);font-size:16px;font-weight:700;margin-bottom:4px}
.footer-contact u{font-weight:700}
.copyright{color:var(--lime);border-top:1px solid var(--footer-line);margin-top:14px;padding-top:11px;font-size:14.5px}
</style>
</head>
<body>
<header class="site-header">
  <div class="brand">
    <span class="brand-square"></span>
    <span class="brand-name">Corvantel</span>
  </div>
</header>

<nav class="main-nav">
  <ul>
    <li class="current">Home</li>
    <li>About</li>
    <li>Accounting &amp; Advisory</li>
    <li>Audit &amp; Assurance</li>
    <li>Corvantel Super</li>
    <li>Careers</li>
    <li>Newsletters</li>
    <li>Contact Us</li>
  </ul>
</nav>

<section class="hero">
  <div class="hero-art" role="img" aria-label="Line illustration of a pen resting on a calculator over a blue building facade"></div>
  <h2 class="hero-title">Accounting and <em>Tax</em><br><em>Audit</em> and Assurance<br>Self Managed <em>Super</em></h2>
  <div class="hero-actions">
    <div class="btn btn-green"><span>Send a Enquiry</span>
      <svg class="btn-icon" viewBox="0 0 20 20"><circle cx="10" cy="10" r="9" fill="#fff"/><path d="M8 5.5 13 10 8 14.5z" fill="#4aa544"/></svg></div>
    <div class="btn btn-grey"><span>Contact Us</span>
      <svg class="btn-icon" viewBox="0 0 20 20"><circle cx="10" cy="10" r="9" fill="#fff"/><path d="M8 5.5 13 10 8 14.5z" fill="#6a6a6a"/></svg></div>
  </div>
</section>

<section class="intro">
  <h1>Commitment to Deliver</h1>
  <p>Corvantel is a Tasmanian based firm which offers the skills of Accountants, Business Performance Advisers, Auditors and Self Managed Super Fund Specialists. We strive to surpass the expectations you might have of traditional accounting firms. The strength of our client relationships is evidence that we consistently deliver to that standard.</p>
  <p>If you are ready to change to a better way of looking at your accounting, tax, business, audit or self managed super fund needs, contact us.</p>
  <p>Across the firm we deliver services in a wide range of industries; to individuals, businesses, corporations and financial advisers.</p>
</section>

<aside class="signin">
  <div class="signin-title">
    <svg width="18" height="20" viewBox="0 0 18 20"><path d="M5 9V6a4 4 0 0 1 8 0v3" fill="none" stroke="#1568a8" stroke-width="2.2"/><rect x="2" y="9" width="14" height="10" rx="1.5" fill="#1568a8"/></svg>
    Client Sign in
  </div>
  <div class="signin-tabs">
    <div class="signin-tab active">Accounting</div>
    <div class="signin-tab inactive">Super</div>
  </div>
  <div class="signin-form">
    <label>Username</label>
    <div class="field"></div>
    <label>Password</label>
    <div class="field"></div>
    <div class="signin-actions">
      <div class="btn-login"><span>Login</span><b>»</b></div>
      <span class="forgot">» Forgot password?</span>
    </div>
  </div>
</aside>

<section class="divisions">
  <article class="division">
    <h2>Accounting &amp; Advisory</h2>
    <p>Our Accounting and Advisory team - AG Corvantel Chartered Accountants - provide traditional accounting services and professional corporate and business advice.</p>
    <div class="btn-more"><span>read more</span><b>»</b></div>
  </article>
  <article class="division">
    <h2>Audit &amp; Assurance</h2>
    <p>While the number of firms providing audit services has decreased in recent years, Corvantel remain committed to audit as a core service.</p>
    <div class="btn-more"><span>read more</span><b>»</b></div>
  </article>
  <article class="division">
    <h2>Corvantel Super</h2>
    <p>Corvantel Super is a specialist division formed in July 2009 to service our rapidly growing SMSF client base, in response to the continual growth of the SMSF industry.</p>
    <div class="btn-more"><span>read more</span><b>»</b></div>
  </article>
</section>

<footer class="site-footer">
  <div class="footer-col" style="left:101px">
    <h3>Accounting &amp; Advisory</h3>
    <ul>
      <li>About</li><li>Services</li><li>Tax &amp; Accounting</li><li>Business Advisory</li><li>Family Wealth Management</li><li>Client Sign In</li><li>Calculators</li>
    </ul>
  </div>
  <div class="footer-col" style="left:335px">
    <h3>Corvantel Super</h3>
    <ul>
      <li>About</li><li>Individuals</li><li>Advisers</li><li>Services</li><li>Portal Sign In</li><li>Calculators</li>
    </ul>
  </div>
  <div class="footer-col" style="left:572px">
    <h3>Audit &amp; Assurance</h3>
    <ul>
      <li>About</li><li>Services</li>
      <li class="link-heading">About Corvantel</li>
      <li class="link-heading">Careers @ Corvantel</li>
      <li class="link-heading">Newsletters</li>
      <li class="link-heading">Contact Corvantel</li>
    </ul>
  </div>
  <div class="footer-contact">
    <h3>Get in touch</h3>
    <p>Got a general question or comment?<br>Call or email us using the details below.<br>P: 03 6100 2417 / &nbsp;P: 03 6100 2583<br>Email Us: info@corvantelgroup.com.au<br>Alternatively, <u>send a message</u></p>
    <p class="copyright">© 2011 Corvantel Group. All rights reserved.</p>
  </div>
</footer>
</body>
</html>
```